Super Greens Label for Supplement Bottle

We want to design a front label for a health supplement bottle. The product is called Meadow Twist Chews™. This will be a new product so there is no current website for the product. The focus is on supergreens that taste great and deliver support for energy, digestion, and immune defense.
We want it to be modern, vibrant and appealing.
Bottle size: standard size supplement CLEAR bottle size, with white child resistant cap and the label panel dimensions are 3” x 7”. The label should be primarily white and green, with a touch of red; (see color palettes)/it can also ONLY be white and green. See samples attached.
We are only focused on the front of the bottle design, not on the back, but leave space for the supplement panel and other text on the back.
So the text for the front of the bottle is:
RT Balden's
Meadow Twist Chews™
Super Greens Blend for:
Energy, Digestion, and Immune Support*
60 Gummies | Dietary Supplement
Raspberry Flavor Gummies
Off to side of the label:
Non-GMO
Vegan Friendly
Plant-Based
Gelatin Free
Colors
Designer to choose colors to be used in the design.

```html
<!DOCTYPE html>
<html lang="en">
<head>
<meta charset="UTF-8">
<title>Meadow Twist Chews – Front Label</title>
<link href="https://fonts.googleapis.com/css2?family=Quicksand:wght@500;600;700&display=swap" rel="stylesheet">
<style>
  :root {
    --green-deep: #0f6b34;
    --green-main: #12773a;
    --green-mid: #2e8a36;
    --green-lime: #8fab35;
    --green-bright: #9cbf3a;
    --berry-red: #d0232a;
    --white: #ffffff;
    --badge-bg: #ffffff;
    --badge-ink: #156b35;
    --canvas-bg: #ffffff;
  }
  * { margin: 0; padding: 0; box-sizing: border-box; }
  html, body {
    width: 1200px; height: 1000px; overflow: hidden;
    background: var(--canvas-bg);
    font-family: "Quicksand", sans-serif;
  }
  .canvas { position: relative; width: 1200px; height: 1000px; }
  .label {
    position: absolute; left: 80px; top: 278px;
    width: 1040px; height: 445px;
    background: var(--green-main);
    overflow: hidden;
    color: var(--white);
  }
  .label__front {
    position: absolute; left: 0; top: 0; width: 413px; height: 100%;
    background:
      radial-gradient(ellipse 340px 260px at 300px 400px, var(--green-bright) 0%, #5f9f34 45%, rgba(18,119,58,0) 100%),
      linear-gradient(180deg, var(--green-main) 0%, #1d7e38 60%, #3f9135 100%);
  }
  .label__side-band {
    position: absolute; left: 413px; top: 0; width: 135px; height: 100%;
    background: var(--green-lime);
  }
  .label__accent-bar {
    position: absolute; left: 42px; top: 0; width: 10px; height: 188px;
    background: var(--white);
  }
  .label__tagline {
    position: absolute; left: 70px; top: 34px;
    font-size: 14px; font-weight: 500; line-height: 23px;
  }
  .label__title {
    position: absolute; left: 68px; top: 96px;
    font-weight: 700; line-height: 1;
  }
  .label__title-top { display: block; font-size: 40px; }
  .label__title-bottom { display: block; font-size: 50px; margin-top: 6px; }
  .count {
    position: absolute; left: 70px; top: 207px;
    display: flex; align-items: center; gap: 8px;
  }
  .count__circle {
    width: 82px; height: 82px; border-radius: 50%;
    background: var(--green-deep);
    display: flex; align-items: center; justify-content: center;
    font-size: 38px; font-weight: 700;
  }
  .count__text { line-height: 1.1; margin-top: -18px; }
  .count__unit { display: block; font-size: 24px; font-weight: 700; }
  .count__type { display: block; font-size: 15px; font-weight: 600; margin-top: 2px; }
  .fruit-art {
    position: absolute; left: 66px; top: 296px;
    width: 198px; height: 118px; border-radius: 48px;
    background: radial-gradient(ellipse at 55% 45%, #e83a55 0%, #c51f3d 55%, rgba(60,110,40,0.6) 100%);
  }
  .flavor-pill {
    position: absolute; left: 156px; top: 278px;
    width: 164px; height: 34px; border-radius: 17px;
    background: var(--berry-red);
    display: flex; align-items: center; justify-content: center;
    font-size: 15px; font-weight: 700;
  }
  .badge {
    position: absolute; width: 70px; height: 70px; border-radius: 50%;
    background: var(--badge-bg);
    box-shadow: 0 2px 4px rgba(0,0,0,0.25);
    display: flex; flex-direction: column; align-items: center; justify-content: center;
    color: var(--badge-ink);
    font-size: 8px; font-weight: 700; text-align: center; line-height: 1.1;
  }
  .badge svg { width: 30px; height: 30px; margin-bottom: 3px; }
  .badge--gelatin { left: 327px; top: 281px; }
  .badge--vegan { left: 287px; top: 356px; }
  .badge--plant { left: 366px; top: 356px; }
  .badge--gmo { left: 447px; top: 356px; }
  .side-count {
    position: absolute; left: 528px; top: 50px;
    width: 320px; height: 88px;
    transform: rotate(90deg); transform-origin: top left;
    display: flex; align-items: center; gap: 8px;
  }
  .side-count .count__circle { width: 80px; height: 80px; font-size: 38px; }
  .side-count .count__text { margin-top: 0; }
  .side-count .count__unit { font-size: 24px; }
  .side-count .count__type { font-size: 14px; }
</style>
</head>
<body>
<div class="canvas">
  <section class="label">
    <div class="label__front"></div>
    <div class="label__side-band"></div>
    <div class="label__accent-bar"></div>

    <p class="label__tagline">Super Greens Blend for:<br>Energy, Digestion, Immune Support</p>

    <h1 class="label__title">
      <span class="label__title-top">Meadow Twist</span>
      <span class="label__title-bottom">Chews</span>
    </h1>

    <div class="count">
      <div class="count__circle">60</div>
      <div class="count__text">
        <span class="count__unit">Gummies</span>
        <span class="count__type">| Dietary Supplement</span>
      </div>
    </div>

    <div class="fruit-art" role="img" aria-label="Photo of fresh raspberries with a green leaf"></div>
    <div class="flavor-pill">Raspberry Flavor</div>

    <div class="badge badge--gelatin">
      <svg viewBox="0 0 30 30" fill="none" stroke="currentColor" stroke-width="2" stroke-linejoin="round">
        <path d="M8 22 L10 8 Q15 5 20 8 L22 22 Z"/>
        <path d="M12 9 V22 M15 8 V22 M18 9 V22"/>
        <path d="M5 24 H25"/>
      </svg>
      GELATIN<br>FREE
    </div>
    <div class="badge badge--vegan">
      <svg viewBox="0 0 30 30" fill="none" stroke="currentColor" stroke-width="3" stroke-linecap="round" stroke-linejoin="round">
        <path d="M7 9 L14 24 L23 5"/>
        <path d="M19 9 Q25 6 26 3" stroke-width="2"/>
      </svg>
      VEGAN<br>FRIENDLY
    </div>
    <div class="badge badge--plant">
      <svg viewBox="0 0 30 30" fill="currentColor">
        <path d="M15 26 V16" stroke="currentColor" stroke-width="2" fill="none"/>
        <path d="M15 17 Q5 17 4 8 Q13 8 15 17 Z"/>
        <path d="M15 15 Q17 4 27 4 Q26 14 15 15 Z"/>
      </svg>
      PLANT<br>BASED
    </div>
    <div class="badge badge--gmo">
      <svg viewBox="0 0 30 30" fill="none" stroke="currentColor" stroke-width="2">
        <circle cx="15" cy="15" r="12"/>
        <path d="M11 6 Q19 15 11 24 M19 6 Q11 15 19 24"/>
        <path d="M7 7 L23 23"/>
      </svg>
      NON GMO
    </div>

    <div class="side-count">
      <div class="count__circle">60</div>
      <div class="count__text">
        <span class="count__unit">Gummies</span>
        <span class="count__type">| Dietary Supplement</span>
      </div>
    </div>
  </section>
</div>
</body>
</html>
```